Business Card Design Project

Recently had a new logo made up for my company and new business cards done as well. I have attached the logos for your viewing. Additional projects may be needed. Good luck!

Industry/Entity Type

Business

```html
<!DOCTYPE html>
<html lang="en">
<head>
<meta charset="utf-8">
<title>Daniel R. Harlow – Business Card</title>
<link href="https://fonts.googleapis.com/css2?family=Source+Serif+4:wght@400;700&family=Inter:wght@400&display=swap" rel="stylesheet">
<style>
  :root {
    --card-bg: #24242c;
    --gold: #cfbd8c;
    --gold-text: #d6c291;
    --ink: #24242c;
    --white: #ffffff;
  }
  html, body {
    margin: 0;
    padding: 0;
    overflow: hidden;
    background: var(--card-bg);
  }
  .card {
    position: relative;
    width: 1200px;
    height: 686px;
    background: var(--card-bg);
    overflow: hidden;
  }
  .name-band {
    position: absolute;
    left: 0;
    top: 237px;
    width: 571px;
    height: 122px;
    background: var(--gold);
  }
  .name {
    position: absolute;
    left: 32px;
    top: 18px;
    margin: 0;
    font-family: "Source Serif 4", Georgia, serif;
    font-weight: 700;
    font-size: 50px;
    line-height: 1;
    color: var(--ink);
    letter-spacing: 0.2px;
  }
  .role {
    position: absolute;
    left: 31px;
    top: 75px;
    margin: 0;
    font-family: "Inter", Arial, sans-serif;
    font-weight: 400;
    font-size: 25px;
    line-height: 1;
    color: var(--white);
  }
  .contact {
    position: absolute;
    left: 38px;
    top: 518px;
    margin: 0;
    font-family: "Source Serif 4", Georgia, serif;
    font-size: 21px;
    color: var(--gold-text);
    letter-spacing: 0.4px;
  }
  .contact p {
    margin: 0;
    height: 43px;
    line-height: 30px;
  }
  .contact .sep {
    padding: 0 4px;
  }
  .brand {
    position: absolute;
    left: 785px;
    top: 562px;
    display: flex;
    align-items: center;
    gap: 14px;
  }
  .brand-square {
    width: 56px;
    height: 60px;
    box-sizing: border-box;
    border: 3px solid var(--gold);
  }
  .brand-name {
    font-family: "Source Serif 4", Georgia, serif;
    font-weight: 400;
    font-size: 30px;
    letter-spacing: 2px;
    text-transform: uppercase;
    color: var(--gold);
  }
</style>
</head>
<body>
  <div class="card">
    <div class="name-band">
      <h1 class="name">Daniel R. Harlow</h1>
      <p class="role">Estate Planning and Insurance Specialist</p>
    </div>

    <div class="contact">
      <p>P: 555-201-4830<span class="sep">|</span>F: 555-201-4831</p>
      <p>1420 Meridian Avenue, Suite 300E, Westbrook, New York 11000</p>
      <p>dharlow@harlowwealth.com<span class="sep">|</span>www.harlowwealth.com</p>
    </div>

    <div class="brand">
      <div class="brand-square"></div>
      <span class="brand-name">Harlow Wealth Group</span>
    </div>
  </div>
</body>
</html>
```